Business card for Les Brisants-Corail campsite

HORIZONTAL / 85x55
OBJECTIVE
Create a modern, attractive and memorable business card for the Les Brisants-Corail campsite, located on the Île d'Oléron.
The map should make people want to discover the campsite and immediately convey its world: ocean, holidays, nature and conviviality.
VISUAL IDENTITY
The design must be in the same graphic style as our website:
www.lesbrisants-corail.fr
The site is the main reference for the visual atmosphere: colours, typography, shapes, photographs and general universe.
The map and the site must give the impression of belonging to a single brand identity.
A UNIVERSE TO TRANSMIT
• Île d'Oléron
• Atlantic Ocean
• Seaside
• Direct access to the beaches
• Vacation
• Nature
• Family-friendly and welcoming atmosphere
• Relaxation
DESIRED STYLE
Bright, warm, modern, nautical and natural.
We want a creation with a real personality, immediately recognizable, and not a generic camping business card.
FRONT
Prioritize visual impact with:
• Official logo Les Brisants-Corail
• Île d'Oléron
• A strong evocation of the ocean and holidays
• A short and memorable hook
The designer is free to propose their own hook.
BACK
The Coral Breakers
Villages 1 & 2
22 Rue des Mouettes
17390 Port-des-Sables
France
Tel.: +33 5 47 12 38 04
www.lesbrisants-corail. fr
Possibility of discreet integration:
Direct access to the beaches
Mobile homes • Pitches • Accommodation
Le Varech Bar-Restaurant
FORMAT
Double-sided card: 85 × 55 mm.
Horizontal orientation
AVOID
• Overly institutional design
• Overloaded map
• Generic "camping" style
• Too many pictograms
• Accumulation of texts
• Modification or distortion of the official logo
• Graphic design unrelated to the website
CREATIVE FREEDOM
We are looking for an original proposal.
The designer can play with the graphic codes of the ocean, waves, sun, beach and Île d'Oléron, while remaining faithful to the visual identity of the site.
The card must be aesthetically pleasing and original enough to make people want to keep it.
The objective:
See the map → think about the ocean and holidays → remember Les Brisants-Corail → discover the campsite.
Target Market(s)
All targets
Industry/Entity Type
Tourisme
Contact Information for Business Card
adresse, téléphone, email, site internet + réseaux sociaux
Look and feel
Each slider illustrates characteristics of the customer's brand and the style your logo design should communicate.

```html
<!DOCTYPE html>
<html lang="en">
<head>
<meta charset="utf-8">
<title>Les Brisants-Corail – Business Card</title>
<link rel="stylesheet" href="https://fonts.googleapis.com/css2?family=Lato:wght@400;700&display=swap">
<style>
  :root {
    --page-bg: #ececec;
    --card-bg: #ffffff;
    --ink: #333638;
    --ink-soft: #4a4d50;
    --ocean: #3fb4e0;
    --sun: #f4ec3c;
    --leaf: #a4c83e;
    --grass: #5fb85a;
  }
  * { box-sizing: border-box; margin: 0; padding: 0; }
  html, body {
    width: 1200px; height: 1200px; overflow: hidden;
    background: var(--page-bg);
    font-family: "Lato", Arial, sans-serif;
    color: var(--ink);
  }
  .card {
    position: absolute;
    left: 201px;
    width: 799px;
    height: 517px;
    background: var(--card-bg);
    overflow: hidden;
  }
  .card--front { top: 64px; }
  .card--back { top: 619px; }

  /* Front */
  .brand-name {
    position: absolute;
    left: 71px; top: 112px;
    font-size: 46px; font-weight: 700;
    color: var(--ink-soft);
    letter-spacing: 0.5px;
    display: flex; align-items: center; gap: 16px;
  }
  .brand-dot {
    width: 34px; height: 34px; border-radius: 50%;
    background: var(--ocean);
  }
  .corner-wash {
    position: absolute;
    right: 0; bottom: 0;
    width: 345px; height: 375px;
    border-top-left-radius: 100% 100%;
    background: linear-gradient(135deg, var(--sun) 0%, var(--leaf) 50%, var(--grass) 80%, var(--ocean) 100%);
  }
  .contact { position: absolute; left: 71px; top: 320px; list-style: none; }
  .contact li {
    display: flex; align-items: flex-start; gap: 12px;
    font-size: 21px; line-height: 27px;
    margin-bottom: 13px;
  }
  .contact svg { flex: 0 0 16px; width: 16px; height: 18px; margin-top: 4px; fill: var(--ocean); }

  /* Back */
  .sun-field {
    position: absolute; left: 0; top: 0;
    width: 799px; height: 300px;
    border-bottom-left-radius: 50% 100%;
    border-bottom-right-radius: 50% 100%;
    background: linear-gradient(180deg, var(--sun) 0%, var(--sun) 70%, var(--leaf) 100%);
  }
  .offer {
    position: absolute; left: 0; top: 106px; width: 799px;
    text-align: center; font-size: 21px; line-height: 40px;
    color: var(--ink);
  }
  .venue {
    position: absolute; top: 378px;
    width: 210px; text-align: center;
    font-size: 21px; font-weight: 700; line-height: 28px;
    color: var(--ink-soft);
  }
  .venue--one { left: 50px; }
  .venue--two { left: 281px; }
  .venue--three { left: 525px; }
</style>
</head>
<body>

<section class="card card--front">
  <div class="brand-name"><span class="brand-dot"></span>Les Brisants-Corail</div>
  <div class="corner-wash" role="img" aria-label="Brand decoration in yellow, green and ocean blue"></div>
  <ul class="contact">
    <li>
      <svg viewBox="0 0 16 18"><path d="M8 0a6 6 0 0 0-6 6c0 4.5 6 12 6 12s6-7.5 6-12a6 6 0 0 0-6-6zm0 8.5A2.5 2.5 0 1 1 8 3.5a2.5 2.5 0 0 1 0 5z"/></svg>
      <span>22 Rue des Mouettes<br>17390 Port-des-Sables, France</span>
    </li>
    <li>
      <svg viewBox="0 0 16 18"><path d="M3.5 1.5l2.6 0 1.2 3.6-1.7 1.3c.9 2 2.3 3.6 4.2 4.7l1.4-1.7 3.5 1.3v2.7c0 .9-.7 1.6-1.6 1.6C6.4 15 1.9 9.7 1.9 3.1c0-.9.7-1.6 1.6-1.6z"/></svg>
      <span>+33 5 47 12 38 04</span>
    </li>
    <li>
      <svg viewBox="0 0 16 18"><path d="M8 1a7 7 0 1 0 0 14A7 7 0 0 0 8 1zm0 1.6c.8 0 1.8 1.5 2.2 4.4H5.8C6.2 4.1 7.2 2.6 8 2.6zM2.7 7h1.6c0 .7.1 1.4.2 2H2.7a5.4 5.4 0 0 1 0-2zm.6 3.6h1.5c.3 1 .6 1.9 1 2.5a5.4 5.4 0 0 1-2.5-2.5zM8 13.4c-.8 0-1.7-1.1-2.1-2.8h4.2c-.4 1.7-1.3 2.8-2.1 2.8zM10.3 9H5.7c-.1-.6-.1-1.3-.1-2h4.8c0 .7 0 1.4-.1 2zm.4 4.1c.4-.6.8-1.5 1-2.5h1.5a5.4 5.4 0 0 1-2.5 2.5zM11.7 9c.1-.6.2-1.3.2-2h1.6a5.4 5.4 0 0 1 0 2h-1.8z"/></svg>
      <span>www.lesbrisants-corail. fr</span>
    </li>
  </ul>
</section>

<section class="card card--back">
  <div class="sun-field" role="img" aria-label="Brand decoration: sunny yellow field fading to green"></div>
  <p class="offer">Mobile homes • Pitches • Accommodation<br>Le Varech Bar-Restaurant</p>
  <div class="venue venue--one">Les Brisants-Corail<br>Village 1</div>
  <div class="venue venue--two">Les Brisants-Corail<br>Village 2</div>
  <div class="venue venue--three">Le Varech<br>Bar / Restaurant</div>
</section>

</body>
</html>
```